Our Company name is Bluefield Office Cleaning Services. We are a Toronto(GTA) company looking for a brochure that with Logo design that gives a description of what we do.

We are a company that specializes in cleaning and sanitizing office/ workplaces. Our Experience includes working with school boards and hospitals, and have 15 plus years experience. We are looking for a simple design that catches and explains to our customers what we offer with some pics, which you can provide.

if you have any questions please let us know.

thank you

Target Market(s)

We are focusing Businesses

Font styles to use
Serif

Colors

Designer to choose colors to be used in the design.

Requirements
Must have
• Must have our name/Logo, brief description of what we do. Contact numbers, (416)-555-0183/ (647)555-0927 email (bluefieldofficecleaningservices@mailbox-example.com
• Pics which you can provide
Nice to have
• We trust your imagination on this

```html
<!DOCTYPE html>
<html lang="en">
<head>
<meta charset="utf-8">
<title>Bluefield Office Cleaning Services – Trifold Brochure</title>
<link rel="stylesheet" href="https://fonts.googleapis.com/css2?family=Open+Sans:wght@400;600;700;800&display=swap">
<style>
:root{
  --bg:#d6d6d6;
  --paper:#ffffff;
  --blue:#1b7fc4;
  --blue-dark:#0f5d99;
  --green:#7cc242;
  --ink:#3d4650;
  --muted:#7b8590;
  --photo-a:#dfe6e4;
  --photo-b:#8fb7c9;
  --photo-c:#5d8a3e;
}
*{margin:0;padding:0;box-sizing:border-box}
html,body{width:1200px;height:2348px;overflow:hidden;background:var(--bg);font-family:"Open Sans",Arial,sans-serif;color:var(--ink)}
.canvas{position:relative;width:1200px;height:2348px}
.row{position:absolute;left:0;width:1200px;height:700px}
.row-cover{top:62px}
.row-outside{top:824px}
.row-inside{top:1586px}
.spread{position:absolute;left:150px;top:0;width:900px;height:700px;display:flex;box-shadow:0 10px 30px rgba(0,0,0,.18)}
.panel{position:relative;width:300px;height:700px;background:var(--paper);overflow:hidden}
.spread .panel + .panel{border-left:1px solid #e6e9ec}
.panel-solo{position:absolute;left:450px;top:0;box-shadow:0 10px 30px rgba(0,0,0,.18)}

.brand{position:absolute;left:0;right:0;top:36px;text-align:center}
.brand-dot{width:44px;height:44px;border-radius:50%;background:var(--blue);margin:0 auto 10px}
.brand-name{font-weight:700;font-size:13px;line-height:1.35;letter-spacing:.06em;color:var(--blue);text-transform:uppercase}

.photo{position:absolute;left:0;width:300px;background:linear-gradient(135deg,var(--photo-a) 0%,var(--photo-b) 55%,var(--photo-c) 100%)}
.swoosh{position:absolute;left:0;width:300px;height:80px;display:block}
.foot-band{position:absolute;left:0;bottom:0;width:300px;height:60px;display:block}

.headline{position:absolute;left:0;right:0;top:520px;padding:0 24px;text-align:right}
.headline h1{font-size:28px;line-height:1.08;font-weight:800;color:var(--blue)}
.headline p{margin-top:6px;font-size:15px;font-weight:600;color:var(--green)}

.tab{position:absolute;left:0;top:28px;height:32px;padding:0 20px;display:flex;align-items:center;background:var(--blue);color:#fff;font-size:14px;font-weight:700;border-radius:0 16px 16px 0}
.section-title{font-size:16px;font-weight:700;color:var(--blue);margin-bottom:8px}
.body-text{font-size:11.5px;line-height:1.6;color:var(--ink)}

.list{list-style:none}
.list li{display:flex;align-items:center;gap:10px;font-size:12.5px;color:var(--ink);padding:6px 0;border-bottom:1px dashed #d5dbe0}
.list li::before{content:"";flex:none;width:10px;height:10px;border-radius:50%;background:var(--green)}

.socials{position:absolute;left:0;right:0;bottom:78px;display:flex;justify-content:center;gap:12px}
.socials span{width:26px;height:26px;border-radius:50%;border:2px solid var(--blue)}

.contact{font-size:12px;line-height:1.5}
.contact .line{display:flex;align-items:center;gap:8px;margin-bottom:6px}
.contact svg{flex:none}
.email{font-size:10px;word-break:break-all;color:var(--blue-dark)}

.call-btn{position:absolute;left:20px;right:20px;bottom:70px;height:64px;border-radius:32px;background:var(--blue);color:#fff;display:flex;flex-direction:column;align-items:center;justify-content:center;text-align:center}
.call-btn strong{font-size:15px;letter-spacing:.04em}
.call-btn span{font-size:12px}
</style>
</head>
<body>
<main class="canvas">

  <!-- Front cover -->
  <section class="row row-cover">
    <article class="panel panel-solo">
      <div class="brand">
        <div class="brand-dot"></div>
        <div class="brand-name">Bluefield Office<br>Cleaning Services</div>
      </div>
      <div class="photo" style="top:150px;height:330px" role="img" aria-label="Smiling cleaner in green apron and yellow gloves with team in an office"></div>
      <svg class="swoosh" style="top:420px" viewBox="0 0 300 80" preserveAspectRatio="none">
        <path d="M0 34 C90 2 200 2 300 22 L300 80 L0 80Z" fill="#fff"/>
        <path d="M0 34 C90 2 200 2 300 22 L300 30 C200 12 90 14 0 44Z" fill="var(--green)"/>
        <path d="M0 48 C90 20 200 18 300 36 L300 42 C200 26 90 28 0 56Z" fill="var(--blue)"/>
      </svg>
      <div class="headline">
        <h1>Lorem ipsum<br>dolor sit amet</h1>
        <p>consectetur adipiscing elit</p>
      </div>
      <svg class="foot-band" viewBox="0 0 300 60" preserveAspectRatio="none">
        <path d="M0 22 C100 0 200 0 300 18 L300 24 C200 8 100 8 0 30Z" fill="var(--green)"/>
        <path d="M0 34 C100 12 200 12 300 28 L300 60 L0 60Z" fill="var(--blue)"/>
      </svg>
    </article>
  </section>

  <!-- Outside spread -->
  <section class="row row-outside">
    <div class="spread">
      <article class="panel">
        <div class="tab">Our Services</div>
        <div class="photo" style="top:80px;height:200px" role="img" aria-label="Team of cleaners in green aprons wiping office desks"></div>
        <svg class="swoosh" style="top:240px" viewBox="0 0 300 80" preserveAspectRatio="none">
          <path d="M0 34 C90 2 200 2 300 22 L300 80 L0 80Z" fill="#fff"/>
          <path d="M0 34 C90 2 200 2 300 22 L300 30 C200 12 90 14 0 44Z" fill="var(--green)"/>
          <path d="M0 48 C90 20 200 18 300 36 L300 42 C200 26 90 28 0 56Z" fill="var(--blue)"/>
        </svg>
        <ul class="list" style="position:absolute;left:28px;right:28px;top:340px">
          <li>Office cleaning</li>
          <li>Floor care</li>
          <li>Washroom sanitizing</li>
          <li>Window washing</li>
          <li>Waste removal</li>
        </ul>
        <div class="socials"><span></span><span></span><span></span><span></span></div>
        <svg class="foot-band" viewBox="0 0 300 60" preserveAspectRatio="none">
          <path d="M0 22 C100 0 200 0 300 18 L300 24 C200 8 100 8 0 30Z" fill="var(--green)"/>
          <path d="M0 34 C100 12 200 12 300 28 L300 60 L0 60Z" fill="var(--blue)"/>
        </svg>
      </article>

      <article class="panel">
        <div class="photo" style="top:0;height:170px;width:150px" role="img" aria-label="Cleaner polishing a glass office partition"></div>
        <div class="photo" style="top:0;left:150px;width:150px;height:170px;background:linear-gradient(135deg,#e8ecea,#9fc48a)" role="img" aria-label="Cleaning crew in green aprons standing together"></div>
        <div style="position:absolute;left:28px;right:28px;top:205px">
          <div class="brand-dot" style="width:34px;height:34px;border-radius:50%;background:var(--blue);margin:0 auto 8px"></div>
          <div class="brand-name" style="text-align:center;margin-bottom:22px">Bluefield Office<br>Cleaning Services</div>
          <div class="section-title">Contact Us</div>
          <p class="body-text" style="margin-bottom:12px">Call us today for a free quote.</p>
          <div class="contact">
            <div class="line"><svg width="14" height="14" viewBox="0 0 24 24"><path d="M6.6 10.8a15 15 0 006.6 6.6l2.2-2.2a1 1 0 011-.25 11.4 11.4 0 003.6.57 1 1 0 011 1V20a1 1 0 01-1 1A17 17 0 013 4a1 1 0 011-1h3.5a1 1 0 011 1c0 1.25.2 2.45.57 3.57a1 1 0 01-.25 1z" fill="var(--blue)"/></svg>(416)-555-0183</div>
            <div class="line"><svg width="14" height="14" viewBox="0 0 24 24"><path d="M6.6 10.8a15 15 0 006.6 6.6l2.2-2.2a1 1 0 011-.25 11.4 11.4 0 003.6.57 1 1 0 011 1V20a1 1 0 01-1 1A17 17 0 013 4a1 1 0 011-1h3.5a1 1 0 011 1c0 1.25.2 2.45.57 3.57a1 1 0 01-.25 1z" fill="var(--blue)"/></svg>(647)555-0927</div>
            <div class="line"><svg width="14" height="14" viewBox="0 0 24 24"><rect x="2" y="5" width="20" height="14" rx="2" fill="none" stroke="var(--blue)" stroke-width="2"/><path d="M3 6l9 7 9-7" fill="none" stroke="var(--blue)" stroke-width="2"/></svg><span class="email">bluefieldofficecleaningservices@mailbox-example.com</span></div>
          </div>
        </div>
        <div class="photo" style="top:520px;height:120px" role="img" aria-label="Cleaner with spray bottle in a bright office"></div>
        <svg class="foot-band" viewBox="0 0 300 60" preserveAspectRatio="none">
          <path d="M0 22 C100 0 200 0 300 18 L300 24 C200 8 100 8 0 30Z" fill="var(--green)"/>
          <path d="M0 34 C100 12 200 12 300 28 L300 60 L0 60Z" fill="var(--blue)"/>
        </svg>
      </article>

      <article class="panel">
        <div class="brand">
          <div class="brand-dot"></div>
          <div class="brand-name">Bluefield Office<br>Cleaning Services</div>
        </div>
        <div class="photo" style="top:150px;height:330px" role="img" aria-label="Smiling cleaner in green apron and yellow gloves with team in an office"></div>
        <svg class="swoosh" style="top:420px" viewBox="0 0 300 80" preserveAspectRatio="none">
          <path d="M0 34 C90 2 200 2 300 22 L300 80 L0 80Z" fill="#fff"/>
          <path d="M0 34 C90 2 200 2 300 22 L300 30 C200 12 90 14 0 44Z" fill="var(--green)"/>
          <path d="M0 48 C90 20 200 18 300 36 L300 42 C200 26 90 28 0 56Z" fill="var(--blue)"/>
        </svg>
        <div class="headline">
          <h1>Lorem ipsum<br>dolor sit amet</h1>
          <p>consectetur adipiscing elit</p>
        </div>
        <svg class="foot-band" viewBox="0 0 300 60" preserveAspectRatio="none">
          <path d="M0 22 C100 0 200 0 300 18 L300 24 C200 8 100 8 0 30Z" fill="var(--green)"/>
          <path d="M0 34 C100 12 200 12 300 28 L300 60 L0 60Z" fill="var(--blue)"/>
        </svg>
      </article>
    </div>
  </section>

  <!-- Inside spread -->
  <section class="row row-inside">
    <div class="spread">
      <article class="panel">
        <svg class="swoosh" style="top:0;height:90px" viewBox="0 0 300 80" preserveAspectRatio="none">
          <path d="M0 0 L300 0 L300 30 C200 56 90 60 0 36Z" fill="var(--blue)"/>
          <path d="M0 44 C90 66 200 62 300 40 L300 46 C200 70 90 74 0 52Z" fill="var(--green)"/>
        </svg>
        <div style="position:absolute;left:28px;right:28px;top:120px">
          <div class="section-title">Why Choose Us</div>
          <ul class="list">
            <li>15+ years experience</li>
            <li>School boards and hospitals</li>
            <li>Trained, insured staff</li>
            <li>Eco-friendly products</li>
            <li>Flexible night shifts</li>
            <li>Serving the GTA</li>
          </ul>
        </div>
        <div class="call-btn">
          <strong>CALL NOW</strong>
          <span>(416)-555-0183 · (647)555-0927</span>
        </div>
        <svg class="foot-band" viewBox="0 0 300 60" preserveAspectRatio="none">
          <path d="M0 22 C100 0 200 0 300 18 L300 24 C200 8 100 8 0 30Z" fill="var(--green)"/>
          <path d="M0 34 C100 12 200 12 300 28 L300 60 L0 60Z" fill="var(--blue)"/>
        </svg>
      </article>

      <article class="panel">
        <svg class="swoosh" style="top:0;height:90px" viewBox="0 0 300 80" preserveAspectRatio="none">
          <path d="M0 0 L300 0 L300 36 C200 60 90 56 0 30Z" fill="var(--blue)"/>
          <path d="M0 38 C90 64 200 68 300 44 L300 50 C200 74 90 70 0 46Z" fill="var(--green)"/>
        </svg>
        <div style="position:absolute;left:28px;right:28px;top:120px">
          <div class="section-title">Who We Are</div>
          <p class="body-text" style="margin-bottom:26px">Bluefield Office Cleaning Services is a Toronto company that cleans and sanitizes offices and workplaces across the GTA. For more than fifteen years our teams have kept school boards, hospitals and businesses spotless, safe and ready for work every single day.</p>
          <div class="section-title">What We Do</div>
          <p class="body-text">We offer daily and weekly office cleaning, deep sanitizing of desks, kitchens and washrooms, floor care, window washing and waste removal. Every plan is built around your hours, so your staff arrive to a fresh, healthy space.</p>
        </div>
        <svg class="foot-band" viewBox="0 0 300 60" preserveAspectRatio="none">
          <path d="M0 22 C100 0 200 0 300 18 L300 24 C200 8 100 8 0 30Z" fill="var(--green)"/>
          <path d="M0 34 C100 12 200 12 300 28 L300 60 L0 60Z" fill="var(--blue)"/>
        </svg>
      </article>

      <article class="panel">
        <div class="photo" style="top:0;height:220px;background:linear-gradient(135deg,#1d2630 0%,#4a5561 55%,#d8b233 100%)" role="img" aria-label="Gloved hand wiping a dark office surface"></div>
        <svg class="swoosh" style="top:170px" viewBox="0 0 300 80" preserveAspectRatio="none">
          <path d="M0 34 C90 2 200 2 300 22 L300 80 L0 80Z" fill="#fff"/>
          <path d="M0 34 C90 2 200 2 300 22 L300 30 C200 12 90 14 0 44Z" fill="var(--green)"/>
          <path d="M0 48 C90 20 200 18 300 36 L300 42 C200 26 90 28 0 56Z" fill="var(--blue)"/>
        </svg>
        <div style="position:absolute;left:28px;right:28px;top:280px">
          <div class="section-title">Our Promise</div>
          <p class="body-text">Our trained and insured cleaners follow hospital-grade sanitizing standards. We use safe products, check every job and respond quickly to your requests, so you can focus on running your business.</p>
        </div>
        <svg class="foot-band" viewBox="0 0 300 60" preserveAspectRatio="none">
          <path d="M0 22 C100 0 200 0 300 18 L300 24 C200 8 100 8 0 30Z" fill="var(--green)"/>
          <path d="M0 34 C100 12 200 12 300 28 L300 60 L0 60Z" fill="var(--blue)"/>
        </svg>
      </article>
    </div>
  </section>

</main>
</body>
</html>
```